"Beyond Marrow Cay" Fictional Book Cover

BEYOND MARROW CAY
By: Dale Pruitt

Here's the intro .

"It had been nearly forty years since Ted Larraby last went to the island from where he was raised. Three months earlier he never would have thought about ever coming back. But life is weird. Things happen quickly and plans change, especially when your very life is at stake. The reason he was going back wasn’t to see old friends...no, no, no. They’re all dead. Of all the kids he grew up with on the island who moved off, he’s the only one still alive. Why?"

Pretty much all just a Lumeno book, by the way.

Target Market(s)

fiction readers

Requirements
Must have
• Somewhat of a dark, mysterious cover is what I'd like to see. Use your imagination. I've never written a fiction book before so I'm very open to ideas

Needs to have my name, DALE PRUITT at the bottom. like my other books, all of which are non-fiction
Nice to have
• Mysterious is what I'm looking for. NOT A HORROR story though. More a guy who left the island years ago, but is being called back to escape the rat race of modern, consumerist culture.

Please remember this NEEDS to jump out as a thumbnail on Bookvale as people are browsing. Mainly the WORDS need to stick out. Lighter words on a say a blue background.

If you want to try to use the attached pic, or something like this, to reflect an island in the cover, that'd be good.

I've also uploaded a couple images I purchased from Pixelcrate, hopefully you can make something work with these.

```html
<!DOCTYPE html>
<html lang="en">
<head>
<meta charset="utf-8">
<title>Beyond Marrow Cay — Dale Pruitt</title>
<link rel="stylesheet" href="https://fonts.googleapis.com/css2?family=Cinzel:wght@400;500&display=swap">
<style>
  :root {
    --sky-top: #0b2247;
    --sky-mid: #163a5a;
    --sky-low: #24506a;
    --sky-horizon: #3d6474;
    --shore-dark: #1f3529;
    --shore-green: #2f4b36;
    --houses: #6f7f80;
    --pier: #8e9898;
    --water-top: #17304b;
    --water-deep: #0a1a33;
    --title-ink: #ffffff;
  }
  html, body {
    margin: 0;
    padding: 0;
    overflow: hidden;
    background: var(--water-deep);
  }
  .cover {
    position: relative;
    width: 750px;
    height: 1200px;
    overflow: hidden;
    font-family: "Cinzel", "Trajan Pro", serif;
  }
  .cover__scene {
    position: absolute;
    inset: 0;
    background: linear-gradient(to bottom,
      var(--sky-top) 0%,
      var(--sky-mid) 28%,
      var(--sky-low) 42%,
      var(--sky-horizon) 51%,
      var(--shore-green) 54%,
      var(--houses) 57%,
      var(--shore-dark) 60%,
      var(--shore-green) 64%,
      var(--houses) 67%,
      var(--pier) 69.5%,
      var(--water-top) 72%,
      #10263f 85%,
      var(--water-deep) 100%);
  }
  .cover__title {
    position: absolute;
    inset: 0;
    margin: 0;
    font-weight: 400;
  }
  .cover__title svg {
    display: block;
    width: 750px;
    height: 700px;
  }
  .cover__title-text {
    fill: var(--title-ink);
    font-family: "Cinzel", "Trajan Pro", serif;
    font-weight: 400;
  }
  .cover__author {
    position: absolute;
    left: 0;
    right: 0;
    top: 1078px;
    margin: 0;
    text-align: center;
    color: var(--title-ink);
    font-size: 64px;
    font-weight: 400;
    letter-spacing: 0.03em;
    line-height: 1;
  }
</style>
</head>
<body>
  <main class="cover">
    <div class="cover__scene" role="img" aria-label="Dusky photograph of an island harbour: dark blue sky, white houses and green trees along the shore, a ferry pier with pilings and moored boats over dark water"></div>
    <h1 class="cover__title">
      <svg viewBox="0 0 750 700" aria-label="Beyond Marrow Cay">
        <defs>
          <filter id="title-glow" x="-10%" y="-20%" width="120%" height="140%">
            <feGaussianBlur in="SourceAlpha" stdDeviation="5" result="blur"/>
            <feFlood flood-color="#ffffff" flood-opacity="0.8"/>
            <feComposite in2="blur" operator="in" result="glow"/>
            <feMerge>
              <feMergeNode in="glow"/>
              <feMergeNode in="SourceGraphic"/>
            </feMerge>
          </filter>
        </defs>
        <g filter="url(#title-glow)">
          <text class="cover__title-text" x="375" y="218" font-size="158" text-anchor="middle" textLength="600" lengthAdjust="spacingAndGlyphs">BEYOND</text>
          <text class="cover__title-text" x="377" y="405" font-size="192" text-anchor="middle" textLength="612" lengthAdjust="spacingAndGlyphs">MARROW</text>
          <text class="cover__title-text" x="375" y="612" font-size="240" text-anchor="middle" textLength="560" lengthAdjust="spacingAndGlyphs">CAY</text>
        </g>
      </svg>
    </h1>
    <p class="cover__author">Dale Pruitt</p>
  </main>
</body>
</html>
```